Derek Mavlow Business card

Hey there, I’m hoping to have a business card designed. I’m in Real estate and just switched to a new Brokerage called: The Property Quarter

The back could just be the company name maybe or whatever looks good!

I’ve attached some logos of our company and some cards my buddy had done up.

On the card:
Derek Mavlow
derekmavlow@postnest.example
587-204-6618
derekmavlow-homes.example

Target Market(s)

Home buyers and sellers

Industry/Entity Type

Real Estate

Contact Information for Business Card

just looking for a cool and modern design with my picture on it. I like the idea of Black and red being used.

Requirements
Must have
• all the details provided. I'm open to anything. Just want a professional looking card.

```html
<!DOCTYPE html>
<html lang="en">
<head>
<meta charset="utf-8">
<title>Derek Mavlow – Business Card</title>
<link href="https://fonts.googleapis.com/css2?family=Fira+Sans:wght@400;600;700;800&display=swap" rel="stylesheet">
<style>
  :root {
    --page-bg: #1b1b1b;
    --card-black: #000000;
    --card-edge: #2a2a2a;
    --brand-red: #d6193a;
    --ink-white: #f2f2f4;
    --photo-dark: #141414;
    --photo-mid: #3a3a3c;
  }
  * { box-sizing: border-box; margin: 0; padding: 0; }
  html, body {
    width: 1200px; height: 750px; overflow: hidden;
    background: var(--page-bg);
    font-family: "Fira Sans", Arial, sans-serif;
    color: var(--ink-white);
  }
  .sheet {
    position: relative; width: 1200px; height: 750px;
    display: flex; align-items: center; justify-content: center; gap: 24px;
  }
  .card {
    position: relative; width: 552px; height: 368px;
    background: var(--card-black);
    border: 1px solid var(--card-edge);
    overflow: hidden;
  }
  /* Front */
  .brand-name {
    position: absolute; left: 40px; top: 52px;
    font-weight: 800; font-size: 30px; line-height: 1.05;
    color: var(--ink-white); letter-spacing: -0.5px;
    text-transform: uppercase;
  }
  .portrait {
    position: absolute; right: 0; top: 0;
    width: 220px; height: 300px;
  }
  .agent {
    position: absolute; left: 40px; top: 178px; width: 300px;
  }
  .agent-name { font-weight: 600; font-size: 22px; line-height: 1.1; }
  .agent-title { font-weight: 600; font-size: 13.5px; margin-top: 2px; }
  .divider {
    position: absolute; left: 40px; top: 234px;
    width: 270px; height: 3px; background: var(--brand-red);
  }
  .contact {
    position: absolute; left: 40px; top: 248px;
    font-size: 14px; line-height: 1.32;
  }
  .contact .company { font-weight: 600; font-size: 14.5px; text-transform: uppercase; }
  /* Back */
  .card-back {
    display: flex; align-items: center; justify-content: center;
    background: linear-gradient(160deg, var(--card-black) 60%, #161616 100%);
  }
  .back-brand {
    font-weight: 800; font-size: 44px; line-height: 1.05;
    color: var(--ink-white); text-transform: uppercase;
    letter-spacing: -0.5px; text-align: left;
  }
</style>
</head>
<body>
  <main class="sheet">
    <section class="card card-front">
      <div class="brand-name">The Property<br>Quarter</div>

      <svg class="portrait" viewBox="0 0 220 300" role="img" aria-label="Portrait photo of Derek Mavlow in a dark suit, leaning on a white stool">
        <defs>
          <linearGradient id="portraitFill" x1="0" y1="0" x2="0" y2="1">
            <stop offset="0" stop-color="var(--photo-dark)"/>
            <stop offset="0.5" stop-color="var(--photo-mid)"/>
            <stop offset="1" stop-color="var(--card-black)"/>
          </linearGradient>
        </defs>
        <rect width="220" height="300" fill="url(#portraitFill)"/>
      </svg>

      <div class="agent">
        <div class="agent-name">Derek Mavlow</div>
        <div class="agent-title">Sales Representative</div>
      </div>
      <div class="divider"></div>
      <div class="contact">
        <div class="company">The Property Quarter</div>
        <div>derekmavlow@postnest.example</div>
        <div>587-204-6618</div>
        <div>derekmavlow-homes.example</div>
      </div>
    </section>

    <section class="card card-back">
      <div class="back-brand">The Property<br>Quarter</div>
    </section>
  </main>
</body>
</html>
```